Accounting Firm

We are a two partner accounting firm. our business name is VELLIS & MORTABE. We are accountants and business consultants.

We need a stationery design for our letterhead, with compliments slip, business card and envelope.

We'd like clean, professional look. I'm 39 years old and my partner is 60+, so we'd like modern yet elegant design. Dark Navy Blue as a primary colour is preferred.

Thank you.
Updates

Hi Guys

No logo.

Thanks

Industry/Entity Type

Accounting

Requirements
Must have
• Firm name :VELLIS & MORTABE
Business Consultants & Accountants
Address: Level 2 Units 3 & 4, 17 Bramwell Crescent BRAMLEIGH SA 5069
Box address: PO Box 418 ASHCOTT SA 5072
telp: +61 8 8590 4127
fax: +61 8 8642 7715

Dominic Vellis, CA
Tobias Mortabe, CPA

dominic.vellis@vellismortabe.example.au
tobias.mortabe@vellismortabe.example.au

Dark Navy Blue as primary colour

```html
<!DOCTYPE html>
<html lang="en">
<head>
<meta charset="utf-8">
<title>Vellis &amp; Mortabe — Stationery</title>
<link rel="stylesheet" href="https://fonts.googleapis.com/css2?family=EB+Garamond:wght@400;500&display=swap">
<style>
  :root {
    --navy: #1b2466;
    --stripe-deep: #3a63c4;
    --stripe-mid: #86b5ec;
    --stripe-pale: #d6f0fb;
    --paper: #ffffff;
    --edge: #bfe4ee;
    --ink: #3a3f55;
    --text-font: "EB Garamond", Georgia, serif;
  }
  * { box-sizing: border-box; margin: 0; padding: 0; }
  html, body { width: 1200px; height: 900px; overflow: hidden; background: var(--paper); }
  .sheet-board { position: relative; width: 1200px; height: 900px; }

  .brand-header { position: absolute; left: 33px; top: 18px; }
  .brand-header .brand-name { font-family: var(--text-font); font-weight: 500; font-size: 58px; line-height: 1; color: var(--navy); }
  .brand-header .brand-tagline { font-family: var(--text-font); font-size: 27px; color: var(--navy); margin-top: 4px; margin-left: 14px; }

  .piece { position: absolute; background: var(--paper); border: 1px solid var(--edge); overflow: hidden; }
  .band { position: absolute; left: 0; background: var(--navy); }
  .stripes { position: absolute; display: flex; }
  .stripes span { flex: 1; }
  .stripes span:nth-child(1) { background: var(--stripe-deep); }
  .stripes span:nth-child(2) { background: var(--stripe-mid); }
  .stripes span:nth-child(3) { background: var(--stripe-pale); }

  .wordmark { position: absolute; }
  .wordmark .name { font-family: var(--text-font); font-weight: 500; color: var(--navy); line-height: 1; }
  .wordmark .tagline { font-family: var(--text-font); color: var(--navy); line-height: 1.1; }

  .contact { position: absolute; font-family: var(--text-font); color: var(--ink); line-height: 1.35; }

  /* business card */
  .business-card { left: 214px; top: 124px; width: 318px; height: 180px; }
  .business-card .stripes { left: 13px; top: 32px; width: 132px; height: 131px; }
  .business-card .band { top: 163px; width: 100%; height: 13px; }
  .business-card .wordmark { left: 12px; top: 6px; }
  .business-card .wordmark .name { font-size: 15px; }
  .business-card .wordmark .tagline { font-size: 8px; }
  .business-card .holder { position: absolute; left: 160px; top: 52px; font-family: var(--text-font); color: var(--navy); }
  .business-card .holder .person { font-size: 15px; font-weight: 500; }
  .business-card .holder .email { font-size: 7px; color: var(--ink); margin-top: 3px; }
  .business-card .contact { left: 160px; top: 104px; font-size: 7px; }

  /* letterhead */
  .letterhead { left: 562px; top: 112px; width: 585px; height: 758px; }
  .letterhead .band-top { top: 0; width: 100%; height: 35px; }
  .letterhead .band-foot { top: 743px; width: 100%; height: 9px; }
  .letterhead .stripes { left: 42px; top: 0; width: 146px; height: 50px; }
  .letterhead .wordmark { left: 44px; top: 56px; }
  .letterhead .wordmark .name, .compliments-slip .wordmark .name { font-size: 17px; }
  .letterhead .wordmark .tagline, .compliments-slip .wordmark .tagline { font-size: 10px; }
  .letterhead .contact, .compliments-slip .contact { left: 44px; font-size: 6.5px; }
  .letterhead .contact { top: 84px; }

  /* compliments slip */
  .compliments-slip { left: 27px; top: 318px; width: 555px; height: 264px; }
  .compliments-slip .band-top { top: 0; width: 100%; height: 35px; }
  .compliments-slip .stripes { left: 40px; top: 0; width: 144px; height: 50px; }
  .compliments-slip .wordmark { left: 42px; top: 53px; }
  .compliments-slip .contact { top: 82px; left: 42px; }
  .compliments-slip .band-foot { top: 240px; width: 100%; height: 24px; display: flex; align-items: center; justify-content: flex-end; padding-right: 12px; font-family: var(--text-font); font-size: 10px; color: var(--paper); }

  /* envelope */
  .envelope { left: 207px; top: 597px; width: 591px; height: 293px; }
  .envelope .band-top { top: 0; width: 585px; height: 33px; }
  .envelope .stripes { left: 42px; top: 0; width: 145px; height: 171px; }
  .envelope .wordmark { left: 44px; top: 175px; }
  .envelope .wordmark .name { font-size: 18px; }
  .envelope .wordmark .tagline { font-size: 10px; }
  .envelope .contact { left: 44px; top: 204px; font-size: 6.5px; }
</style>
</head>
<body>
<main class="sheet-board">

  <header class="brand-header">
    <div class="brand-name">VELLIS &amp; MORTABE</div>
    <div class="brand-tagline">Business Consultants &amp; Accountants</div>
  </header>

  <section class="piece letterhead" aria-label="Letterhead">
    <div class="band band-top"></div>
    <div class="stripes"><span></span><span></span><span></span></div>
    <div class="wordmark">
      <div class="name">VELLIS &amp; MORTABE</div>
      <div class="tagline">Business Consultants &amp; Accountants</div>
    </div>
    <div class="contact">
      <div>Level 2 Units 3 &amp; 4, 17 Bramwell Crescent BRAMLEIGH SA 5069</div>
      <div>PO Box 418 ASHCOTT SA 5072</div>
      <div>Telp: +61 8 8590 4127</div>
      <div>Fax: +61 8 8642 7715</div>
    </div>
    <div class="band band-foot"></div>
  </section>

  <section class="piece business-card" aria-label="Business card">
    <div class="wordmark">
      <div class="name">VELLIS &amp; MORTABE</div>
      <div class="tagline">Business Consultants &amp; Accountants</div>
    </div>
    <div class="stripes"><span></span><span></span><span></span></div>
    <div class="holder">
      <div class="person">Dominic Vellis, CA</div>
      <div class="email">dominic.vellis@vellismortabe.example.au</div>
    </div>
    <div class="contact">
      <div>Level 2 Units 3 &amp; 4, 17 Bramwell Crescent</div>
      <div>BRAMLEIGH SA 5069</div>
      <div>PO Box 418 ASHCOTT SA 5072</div>
      <div>Telp: +61 8 8590 4127</div>
      <div>Fax: +61 8 8642 7715</div>
    </div>
    <div class="band"></div>
  </section>

  <section class="piece compliments-slip" aria-label="Compliments slip">
    <div class="band band-top"></div>
    <div class="stripes"><span></span><span></span><span></span></div>
    <div class="wordmark">
      <div class="name">VELLIS &amp; MORTABE</div>
      <div class="tagline">Business Consultants &amp; Accountants</div>
    </div>
    <div class="contact">
      <div>Level 2 Units 3 &amp; 4, 17 Bramwell Crescent BRAMLEIGH SA 5069</div>
      <div>PO Box 418 ASHCOTT SA 5072</div>
      <div>Telp: +61 8 8590 4127</div>
      <div>Fax: +61 8 8642 7715</div>
    </div>
    <div class="band band-foot">With Compliments</div>
  </section>

  <section class="piece envelope" aria-label="Envelope">
    <div class="band band-top"></div>
    <div class="stripes"><span></span><span></span><span></span></div>
    <div class="wordmark">
      <div class="name">VELLIS &amp; MORTABE</div>
      <div class="tagline">Business Consultants &amp; Accountants</div>
    </div>
    <div class="contact">
      <div>Level 2 Units 3 &amp; 4, 17 Bramwell Crescent BRAMLEIGH SA 5069</div>
      <div>PO Box 418 ASHCOTT SA 5072</div>
      <div>Telp: +61 8 8590 4127</div>
      <div>Fax: +61 8 8642 7715</div>
    </div>
  </section>

</main>
</body>
</html>
```